Re-design of veterinary clinic website *

For a future relaunch of our webpage, we would like to find a fresh design that still incorporates the spirit of our current one which can be found at http://dr-wenzlaff.de
We are a small business that appeals to locals but are known in a wide area for specialist services.
According to analytics data, most people rarely read through the full website but are using it to inform themselves about opening hours, Telephone numbers and location. Still, the website needs to offer enough content to be ranked positively by the Quandle algorithm.
Our logo is not part of the re-design but needs to be included in your proposal as is. It can be used a source of inspiration, just as the current design. Keep in mind, that the design will be used as the basis of a fluid webdesign for both mobile and desktop. Roughly 75% of our users are on mobile devices.
Target Market(s)
Locals
Industry/Entity Type
Veterinary
Number of Pages Required
1 page
Look and feel
Each slider illustrates characteristics of the customer's brand and the style your logo design should communicate.

```html
<!DOCTYPE html>
<html lang="en">
<head>
<meta charset="utf-8">
<title>Dr. med. vet. Konrad Albers – Small Animal Practice</title>
<link href="https://fonts.googleapis.com/css2?family=Montserrat:ital,wght@0,400;0,600;0,700;1,600&family=Open+Sans:wght@400;600&display=swap" rel="stylesheet">
<style>
:root{
  --blue:#2f7fc1;
  --blue-dark:#1f5f98;
  --sky:#8ecbe9;
  --sky-light:#b9e0f3;
  --ink:#2f3337;
  --muted:#7b8188;
  --line:#d9dde1;
  --paper:#ffffff;
  --mist:#f2f3f4;
  --footer:#f4f5f7;
}
*{box-sizing:border-box;margin:0;padding:0}
html,body{width:1200px;height:2684px;overflow:hidden;background:var(--paper)}
body{position:relative;font-family:"Open Sans",Arial,sans-serif;color:var(--ink);font-size:14px;line-height:1.6}
h1,h2,h3,h4,.nav,.btn,.brand{font-family:"Montserrat",Arial,sans-serif}
.abs{position:absolute}

/* header */
.brand{left:120px;top:22px;display:flex;align-items:center;gap:10px;color:var(--blue);font-weight:600;font-size:15px;line-height:1.2}
.brand .dot{width:34px;height:34px;border-radius:50%;background:var(--sky)}
.brand small{display:block;font-size:11px;color:var(--muted);font-weight:600}
.call{right:290px;top:30px;font-size:13px;font-weight:600;color:var(--blue);white-space:nowrap}
.call span{color:var(--muted);font-weight:400}
.btn{display:inline-block;border-radius:20px;font-size:12px;font-weight:600;padding:8px 22px;border:2px solid var(--blue);color:var(--blue);background:transparent;line-height:1.2}
.btn.solid{background:var(--blue);color:#fff}
.btn.soft{background:var(--sky);border-color:var(--sky);color:#fff}
.appt{right:120px;top:24px}
.nav{right:120px;top:68px;display:flex;gap:34px;font-size:14px;color:var(--ink)}
.nav .on{border-bottom:2px solid var(--blue);padding-bottom:4px}

/* hero */
.hero{left:0;top:110px;width:1200px;height:410px;background:var(--mist)}
.hero-photo{left:470px;top:0;width:730px;height:410px;background:linear-gradient(110deg,#eef0ef 0%,#e2ddd6 35%,#d3a66d 70%,#b8824a 100%)}
.hero h1{left:120px;top:240px;font-size:40px;font-weight:700;line-height:1.15;color:var(--ink)}
.hero .btn{left:120px;top:350px}
.dots{left:120px;top:392px;display:flex;gap:8px}
.dots i{width:10px;height:10px;border-radius:50%;background:#b9bec3}
.dots i:first-child{background:var(--blue)}

/* practice */
.practice-photo{left:120px;top:600px;width:360px;height:280px;background:linear-gradient(160deg,#f3f2ee 0%,#dcd8cc 45%,#8aa56c 80%,#6a7f52 100%)}
.practice{left:600px;top:640px;width:480px}
.practice h2{font-size:24px;font-weight:600;margin-bottom:16px}
.practice p{color:var(--muted);font-size:13px;margin-bottom:12px}
.practice .btn{margin-top:8px}

/* services */
.band{left:0;top:1040px;width:1200px;height:270px;background:var(--sky)}
.band h2{position:absolute;left:0;top:40px;width:1200px;text-align:center;color:#fff;font-size:28px;font-weight:600;line-height:1.3}
.band p{position:absolute;left:380px;top:92px;width:440px;text-align:center;color:#fff;font-size:13px;line-height:1.5}
.card{top:1205px;width:284px}
.card .photo{height:200px}
.card h3{font-size:17px;font-weight:600;margin:30px 0 10px}
.card p{font-size:13px;color:var(--muted);margin-bottom:20px;min-height:62px}
.arrow{top:1266px;width:30px;height:30px}

/* team */
.team-h{left:120px;top:1690px;font-size:28px;font-weight:600}
.team-nav{right:120px;top:1694px;display:flex;gap:8px}
.member{top:1760px;width:170px;text-align:center}
.member .face{width:160px;height:160px;border-radius:50%;margin:0 auto 16px}
.member h4{font-size:13px;font-weight:600}
.show{left:540px;top:1996px;width:120px;text-align:center}

/* footer */
.footer{left:0;top:2100px;width:1200px;height:400px;background:var(--footer)}
.col{top:2150px;width:280px}
.col h3{font-size:24px;font-style:italic;font-weight:600;margin-bottom:26px}
.hours{width:100%;border-collapse:collapse;font-size:12px}
.hours td{padding:6px 0;border-bottom:1px solid var(--line)}
.hours td:first-child{font-weight:600}
.contact p{font-size:12px;color:var(--muted);margin-bottom:18px;line-height:1.5}
.contact .tel{font-size:16px;font-weight:600;color:var(--blue)}
.map{width:280px;height:140px;background:linear-gradient(135deg,#2f3b45 0%,#44525e 50%,#2a343d 100%)}
.col-link{top:2418px;font-size:11px;color:var(--blue);border-bottom:1px solid var(--blue);font-family:"Montserrat",Arial,sans-serif;font-weight:600;letter-spacing:.5px;text-transform:uppercase}

/* bottom */
.social{left:0;top:2572px;width:1200px;display:flex;justify-content:center;gap:14px}
.social i{width:32px;height:32px;border-radius:50%;border:2px solid var(--blue)}
.social i:nth-child(3){background:var(--blue)}
.copy{left:0;top:2628px;width:1200px;text-align:center;font-size:11px;color:var(--muted)}
</style>
</head>
<body>

<header>
  <div class="abs brand"><span class="dot"></span><span><small>Dr. med. vet.</small>Konrad Albers</span></div>
  <div class="abs call"><span>Call Us:</span> 0049/612 40 73</div>
  <a class="abs btn soft appt">Get Appointment</a>
  <nav class="abs nav"><span class="on">Home</span><span>Preview</span><span>Team</span><span>Office Hours</span><span>Services</span><span>Contact Us</span></nav>
</header>

<section class="abs hero">
  <div class="abs hero-photo" role="img" aria-label="Veterinarian in a white coat examining a golden dog"></div>
  <h1 class="abs">Best Care for Your<br>Best Friends</h1>
  <a class="abs btn solid">Discover More</a>
  <div class="abs dots"><i></i><i></i><i></i></div>
</section>

<section>
  <div class="abs practice-photo" role="img" aria-label="Bright practice reception with counter and green plants"></div>
  <div class="abs practice">
    <h2>Our Practice</h2>
    <p>Our small animal practice is located in the Rosenhain district, which you reach easily along the B 45, about 500 metres away from the railway station.</p>
    <p>I founded the practice in 1995. The rooms were built in the Rosenhain district in 1998, and we moved into the current larger rooms in the same building.</p>
    <a class="btn">Explore More</a>
  </div>
</section>

<section>
  <div class="abs band">
    <h2>Our Services</h2>
    <p>The practice offers a comprehensive range of care for dogs, cats and small mammals in a calm and friendly setting.</p>
  </div>
  <svg class="abs arrow" style="left:30px" viewBox="0 0 30 30"><path d="M18 8l-7 7 7 7" fill="none" stroke="#fff" stroke-width="2.5"/></svg>
  <svg class="abs arrow" style="left:1140px" viewBox="0 0 30 30"><path d="M12 8l7 7-7 7" fill="none" stroke="#fff" stroke-width="2.5"/></svg>

  <article class="abs card" style="left:120px">
    <div class="photo" role="img" aria-label="White puppy sitting in green grass" style="background:linear-gradient(180deg,#cfd9c4 0%,#eeeeea 45%,#6f9a3f 100%)"></div>
    <h3>Dogs Care</h3>
    <p>We care for dogs of every age, from first vaccinations to check-ups, dental care and gentle treatment for older companions.</p>
    <a class="btn">Read More</a>
  </article>
  <article class="abs card" style="left:458px">
    <div class="photo" role="img" aria-label="Ginger cat resting in the grass" style="background:linear-gradient(180deg,#9cbf6a 0%,#c98a4f 55%,#7ea04a 100%)"></div>
    <h3>Cats Care</h3>
    <p>Cats need calm handling and patience. We offer preventive care, neutering, nutrition advice and treatment in a quiet room.</p>
    <a class="btn solid">Read More</a>
  </article>
  <article class="abs card" style="left:796px">
    <div class="photo" role="img" aria-label="White rabbit sitting on a lawn" style="background:linear-gradient(180deg,#7fa548 0%,#e8e6e0 50%,#5f8a34 100%)"></div>
    <h3>Small Mammals</h3>
    <p>Rabbits, guinea pigs and hamsters receive expert attention, with advice on housing, feeding and regular dental checks.</p>
    <a class="btn">Read More</a>
  </article>
</section>

<section>
  <h2 class="abs team-h">Our Team</h2>
  <div class="abs team-nav">
    <svg width="30" height="30" viewBox="0 0 30 30"><circle cx="15" cy="15" r="13" fill="none" stroke="#b9bec3" stroke-width="2"/><path d="M17 10l-5 5 5 5" fill="none" stroke="#b9bec3" stroke-width="2"/></svg>
    <svg width="30" height="30" viewBox="0 0 30 30"><circle cx="15" cy="15" r="13" fill="var(--blue)"/><path d="M13 10l5 5-5 5" fill="none" stroke="#fff" stroke-width="2"/></svg>
  </div>
  <div class="abs member" style="left:124px"><div class="face" role="img" aria-label="Portrait of Dr. Konrad Albers" style="background:radial-gradient(circle at 50% 40%,#d9b49a,#6b6f74)"></div><h4>Dr. Konrad Albers</h4></div>
  <div class="abs member" style="left:322px"><div class="face" role="img" aria-label="Portrait of Dr. Beate Hollmann" style="background:radial-gradient(circle at 50% 40%,#e0c0a8,#8a8e93)"></div><h4>Dr. Beate Hollmann</h4></div>
  <div class="abs member" style="left:518px"><div class="face" role="img" aria-label="Portrait of Carina Weiss" style="background:radial-gradient(circle at 50% 40%,#9fc6e6,#2f5f98)"></div><h4 style="color:var(--blue)">Carina Weiss</h4></div>
  <div class="abs member" style="left:714px"><div class="face" role="img" aria-label="Portrait of Tanja Riedel" style="background:radial-gradient(circle at 50% 40%,#e5c2a8,#9c6b57)"></div><h4>Tanja Riedel</h4></div>
  <div class="abs member" style="left:910px"><div class="face" role="img" aria-label="Portrait of Sonja Faber" style="background:radial-gradient(circle at 50% 40%,#e2bfa6,#7a3f3a)"></div><h4>Sonja Faber</h4></div>
  <a class="abs btn show">Show All</a>
</section>

<footer>
  <div class="abs footer"></div>
  <div class="abs col" style="left:120px">
    <h3>Office Hours</h3>
    <table class="hours">
      <tr><td>Monday</td><td>9:00 – 11:00</td><td>16:00 – 19:00</td></tr>
      <tr><td>Tuesday</td><td>9:00 – 11:00</td><td>16:00 – 19:00</td></tr>
      <tr><td>Wednesday</td><td>9:00 – 11:00</td><td>16:00 – 19:00</td></tr>
      <tr><td>Thursday</td><td></td><td>16:00 – 19:00</td></tr>
      <tr><td>Friday</td><td>9:00 – 11:00</td><td>16:00 – 19:00</td></tr>
      <tr><td>Saturday</td><td>10:00 – 12:00</td><td></td></tr>
    </table>
  </div>
  <div class="abs col contact" style="left:460px">
    <h3>Contact Us</h3>
    <p><span class="tel">0049/612 40 73</span><br>Email: info@albers-tierarzt.de</p>
    <p>Fax: 0049/612 40 74</p>
    <p>Birkenweg 12, 63517 Talheim<br>Germany</p>
  </div>
  <div class="abs col" style="left:800px">
    <h3>Directions</h3>
    <div class="map" role="img" aria-label="Street map showing the practice location"></div>
  </div>
  <span class="abs col-link" style="left:120px">Print Hours</span>
  <span class="abs col-link" style="left:460px">Contact Form</span>
  <span class="abs col-link" style="left:800px">Get Directions</span>

  <div class="abs social"><i></i><i></i><i></i><i></i><i></i></div>
  <p class="abs copy">© 2015 Dr. med. vet. Konrad Albers · All rights reserved · Privacy policy</p>
</footer>

</body>
</html>
```